Affiliate website design and wireframe

We need a design of an affiliate website for an application we purchased, it is important that you build the website pages according to the developer of the applications specifications (please see attached documents) the developer of the application will configure the pages and add them to the site. Please take special note of his comments below.

We all so need you to create a wire frame so the developer can test everything (http://sketchwire.tolvaro.vn/)

It will be the homepage and about 16 inner pages (please see attached files)
Here is our website http://bluvendmarket.com/affiliate/affiliates/index.php

The version of the software we purchased is the Kivo Partner Hubline version

Comments from the developers

1. I will need the source files of the design (photoshop .psd files and font files if custom fonts are used), since the implementation is closely bound to component sizes (like border width, margin width etc.) and colors. If you own a corporate design manual, it's crucial to send it as well. Also, please, make sure if you use custom fonts, that these allow legal website integration (like google web fonts).

2. Any and every content is controlled via templates. All editing/adding/removing etc. is done here. The template files are essentially html/php documents, they use a template engine called quillo (http://www.quillo.net/) which has it's own language similar to php.

3. .psd files are ideal, because we deal with the specifics of KPX/KPH implementation on a daily basis. Any html/css developed in advance may prove to be a poor choice. You may choose to let an in-house developer do the job, but experience wise this is more costly, since he will not be accustomed to the template/functionality systems of KPX/KPH.

4. I will need the source files of the design (photoshop .psd files and font files if custom fonts are used), since the implementation is closely bound to component sizes (like border width, margin width etc.) and colors. If you own a corporate design manual, it's crucial to send it as well. Also, please, make sure if you use custom fonts, that these allow legal website integration (like google web fonts).

Regards,

Dorek Hanval
Multimedia Design

We prefer illustrations more than pictures of real people.

This is the home page, it is asking for Merchant and Affiliate sign up, not just affiliate.

http://bluvendmarket.com/affiliate/index.php

Please note the home page features both Merchant and Affiliate sign up

We are looking for illustration design not just stock images

Please remember the search menu that searches for the available programs, see the example we gave you, look at the search menu at the top of the page http://www.tradelumo.com/

We are reviewing everything, no need to send more designs

Target Market(s)

Natural Products Manufacturers
Natural products Sales reps
Natural Products Bloggers
Social Marketing

Industry/Entity Type

Software

Requirements
Must have
• 1. All links on pages should go to the appropriate pages.
2. Colors can be based on our logo design (look at the attachments)
3. Here is our website http://bluvendmarket.com/affiliate/affiliates/index.php
4. We have attached a drawing of how we think the homepage concept should follow.
5. Main concept of design, is trying to show our sales people (Affiliates) are doing multiple things to advertise and sell the merchants products.(see logo)
6. Need to be able to edit all text and images.
7. Our target audience is Natural product sales people (Advertisers, bloggers, ext) and natural product manufacturers.
8. You can speak to the company who made the application, through live chat, on there website http://www.kivopartnerhubline.com/
Nice to have
• See Attached Documents.
site should take up whole website pages
Look For fun Illustrated Website, one of the better ones we have seen is http://www.tradelumo.com/index.cfm
Should not have
• Please look very carefully at developers comment above.

```html
<!DOCTYPE html>
<html lang="en">
<head>
<meta charset="utf-8">
<title>Bluvendmarket – Affiliate Home</title>
<link href="https://fonts.googleapis.com/css2?family=Open+Sans:wght@300;400;600;700&display=swap" rel="stylesheet">
<style>
:root{
  --red:#e8473f;
  --red-dark:#c93a33;
  --yellow:#f4b400;
  --yellow-dark:#d49a00;
  --charcoal:#3a3838;
  --maroon:#4b1717;
  --nav:#6b6b6b;
  --nav-active:#888888;
  --pattern-red:#c24b4b;
  --band:#dcdcdc;
  --page:#f4f4f4;
  --panel:#f8f8f8;
  --footer:#3c3c3e;
  --footer-text:#8c8c8c;
  --text:#444;
  --muted:#8a8a8a;
  --feature:#e9e9e9;
}
*{box-sizing:border-box;margin:0;padding:0}
html,body{width:1200px;height:936px;overflow:hidden}
body{position:relative;background:var(--page);font-family:"Open Sans",Arial,sans-serif;color:var(--text)}
.band{position:absolute;left:0;width:1200px}
.band-top{top:0;height:78px;background:#e6e6e6}
.band-nav{top:78px;height:41px;background:var(--nav)}
.band-hero{top:119px;height:267px;background:var(--pattern-red)}
.band-call{top:386px;height:79px;background:var(--band)}
.band-footer{top:771px;height:165px;background:var(--footer)}
.wrap{position:absolute;left:229px;width:742px}

/* header */
.site-header{top:0;height:78px;background:#fff}
.site-header svg{position:absolute;left:0;top:0}
.brand{position:absolute;left:58px;top:28px;display:flex;align-items:center;gap:8px;font-weight:700;font-size:16px;color:#2f5aa8}
.brand-dot{width:18px;height:18px;border-radius:50%;background:#2f5aa8}
.btn{position:absolute;display:flex;align-items:center;justify-content:center;font-size:14px;font-weight:300;border-radius:3px;color:#fff;box-shadow:0 2px 2px rgba(0,0,0,.3)}
.btn-red{background:var(--red);border:1px solid var(--red-dark)}
.btn-yellow{background:var(--yellow);border:1px solid var(--yellow-dark);color:#3a2a00}
.login-affiliate{left:485px;top:31px;width:98px;height:29px}
.login-merchant{left:591px;top:31px;width:112px;height:29px}

/* nav */
.main-nav{top:78px;height:41px}
.main-nav ul{list-style:none;display:flex;height:41px}
.main-nav li{padding:0 12px;line-height:41px;color:#fff;font-size:14px;font-weight:300}
.main-nav li.active{background:var(--nav-active);padding:0 16px 0 20px}
.follow{position:absolute;left:553px;top:0;height:41px;display:flex;align-items:center;gap:9px;color:#fff;font-size:13px;font-weight:700}
.follow i{display:block;width:8px;height:8px;border-radius:50%;background:#fff}

/* hero */
.hero{top:119px;height:267px;background:var(--charcoal);overflow:hidden}
.hero svg{position:absolute;left:0;top:0}
.hero-copy{position:absolute;left:16px;top:66px;width:270px}
.hero-title{font-size:25px;font-weight:700;color:var(--yellow);letter-spacing:-.5px;line-height:30px}
.hero-sub{font-size:31px;font-weight:300;color:var(--red);letter-spacing:-.6px;line-height:34px}
.hero-text{margin-top:6px;font-family:Arial,sans-serif;font-size:10.5px;font-weight:700;color:#fff;line-height:12.5px}
.signup-affiliate{left:17px;top:193px;width:98px;height:29px}
.signup-login{left:130px;top:193px;width:97px;height:29px}

/* call band */
.call{top:386px;height:79px;background:var(--band)}
.call-phone{position:absolute;left:26px;top:32px}
.call-number{position:absolute;left:55px;top:32px;font-size:14px;font-weight:300;color:#555}
.call-divider{position:absolute;left:241px;top:17px;width:1px;height:45px;background:#aaa}
.call-text{position:absolute;left:282px;top:21px;width:285px;font-family:Arial,sans-serif;font-size:11px;line-height:13px;color:#555}
.join{left:582px;top:26px;width:98px;height:29px}

/* content */
.content{top:465px;height:330px;background:var(--panel)}
.col{position:absolute;top:0}
.col h2{position:absolute;top:32px;font-size:13px;font-weight:600;display:flex;align-items:center;gap:10px;white-space:nowrap}
.col-who{left:25px;width:200px}
.col-who h2{left:0;color:#333}
.avatar{width:20px;height:20px;border-radius:50%;background:#555}
.col-who p{position:absolute;top:77px;width:200px;font-family:Arial,sans-serif;font-size:11px;line-height:12.3px;color:var(--muted)}
.col-how{left:247px;width:258px;height:320px;background:#fbfbfb;box-shadow:0 0 10px rgba(0,0,0,.06)}
.col-how h2{left:19px;color:var(--red)}
.col-how ul{position:absolute;left:17px;top:67px;width:222px;list-style:none;font-family:Arial,sans-serif;font-size:11px;line-height:15px;color:#444}
.col-how li{position:relative;padding-left:17px}
.col-how li svg{position:absolute;left:0;top:4px}
.col-feature{left:520px;width:205px}
.col-feature h2{left:0;color:#333}
.feature-box{position:absolute;left:2px;width:202px;background:var(--feature);font-size:13px;font-weight:300;color:#444;line-height:16px;padding:1px 4px;display:flex;align-items:center;letter-spacing:-.2px}
.feature-note{position:absolute;left:2px;top:210px;width:205px;font-family:Arial,sans-serif;font-size:11px;line-height:12.5px;color:#333}

/* footer */
.site-footer{top:795px;height:141px}
.footer-title{position:absolute;left:4px;top:33px;color:#fff;font-size:14px;font-weight:600}
.footer-contact{position:absolute;left:4px;top:60px;display:flex;gap:18px;font-family:Arial,sans-serif;font-size:11px;color:var(--footer-text)}
.footer-contact span{display:flex;align-items:center;gap:4px}
.footer-contact i{display:block;width:7px;height:7px;background:var(--footer-text)}
.footer-rule{position:absolute;left:4px;top:82px;width:562px;height:1px;background:#555}
.footer-links{position:absolute;left:4px;top:92px;display:flex;gap:16px;font-family:Arial,sans-serif;font-size:11px;color:var(--footer-text)}
.social-list{position:absolute;left:629px;top:16px;list-style:none;font-family:Arial,sans-serif;font-size:11px;color:var(--footer-text)}
.social-list li{height:19px;display:flex;align-items:center;gap:9px}
.social-list i{display:block;width:6px;height:6px;background:var(--footer-text)}
.footer-base{position:absolute;left:0;top:910px;width:1200px;height:1px;background:#2d2d2f}
.copyright{position:absolute;left:233px;top:917px;font-family:Arial,sans-serif;font-size:10.5px;color:var(--footer-text)}
</style>
</head>
<body>
<div class="band band-top"></div>
<div class="band band-nav"></div>
<div class="band band-hero"></div>
<div class="band band-call"></div>
<div class="band band-footer"></div>

<header class="wrap site-header">
  <svg width="742" height="78" viewBox="0 0 742 78">
    <path d="M322 78 Q370 12 470 0 L742 0 L742 78 Z" fill="#e8473f"/>
    <path d="M338 78 Q386 18 488 0 L742 0 L742 78 Z" fill="#3a3838"/>
  </svg>
  <div class="brand"><span class="brand-dot"></span>BLUVENDMARKET</div>
  <a class="btn btn-red login-affiliate">Affiliate Login</a>
  <a class="btn btn-yellow login-merchant">Merchant Login</a>
</header>

<nav class="wrap main-nav">
  <ul>
    <li class="active">Home</li><li>About Us</li><li>Services</li><li>Partners</li><li>Sign Up</li><li>Contact Us</li>
  </ul>
  <div class="follow">Follow Us: <i></i><i></i><i></i><i></i><i></i></div>
</nav>

<section class="wrap hero">
  <svg width="742" height="267" viewBox="0 0 742 267">
    <path d="M284 0 Q236 190 398 267 L742 267 L742 0 Z" fill="#e8473f"/>
    <path d="M296 0 Q254 185 405 267 L742 267 L742 0 Z" fill="#ffffff"/>
    <path d="M302 0 Q262 183 410 267 L742 267 L742 0 Z" fill="#4b1717"/>
    <g stroke="#c9a5a5" stroke-width="1" stroke-dasharray="3 3" fill="none">
      <line x1="533" y1="131" x2="471" y2="36"/>
      <line x1="533" y1="131" x2="591" y2="36"/>
      <line x1="533" y1="131" x2="419" y2="131"/>
      <line x1="533" y1="131" x2="644" y2="131"/>
      <line x1="533" y1="131" x2="471" y2="222"/>
      <line x1="533" y1="131" x2="591" y2="222"/>
    </g>
    <circle cx="533" cy="131" r="32" fill="#fff"/>
    <text x="533" y="136" text-anchor="middle" font-family="Open Sans, sans-serif" font-size="13" fill="#4b1717">Product</text>
    <g fill="#fff">
      <circle cx="471" cy="36" r="15"/><circle cx="591" cy="36" r="15"/>
      <circle cx="419" cy="131" r="15"/><circle cx="644" cy="131" r="15"/>
      <circle cx="471" cy="222" r="15"/><circle cx="591" cy="222" r="15"/>
    </g>
    <g fill="#4b1717" stroke="#4b1717">
      <!-- share -->
      <circle cx="465" cy="36" r="2.5"/><circle cx="477" cy="30" r="2.5"/><circle cx="477" cy="42" r="2.5"/>
      <path d="M465 36 L477 30 M465 36 L477 42" stroke-width="1.5" fill="none"/>
      <!-- phone -->
      <circle cx="591" cy="36" r="8" fill="none" stroke-width="1.5"/>
      <path d="M587 32 Q588 40 595 41 L596 38 L593 37 L592 38 Q589 37 589 34 L590 33 L589 30 Z" stroke="none"/>
      <!-- feed -->
      <circle cx="415" cy="136" r="2" stroke="none"/>
      <path d="M414 129 A8 8 0 0 1 421 136 M414 124 A13 13 0 0 1 426 136" fill="none" stroke-width="2"/>
      <!-- text message -->
      <rect x="638" y="124" width="10" height="14" rx="1.5" fill="none" stroke-width="1.5"/>
      <rect x="643" y="127" width="7" height="5" rx="1" stroke="none"/>
      <!-- banner -->
      <rect x="464" y="216" width="14" height="9" fill="none" stroke-width="1.5"/>
      <path d="M471 225 L471 230 M467 230 L475 230" fill="none" stroke-width="1.5"/>
      <!-- email -->
      <rect x="584" y="216" width="14" height="11" fill="none" stroke-width="1.5"/>
      <path d="M584 216 L591 222 L598 216" fill="none" stroke-width="1.5"/>
    </g>
    <g font-family="Open Sans, sans-serif" font-size="10" fill="#fff">
      <text x="432" y="33" text-anchor="middle">Social</text>
      <text x="432" y="45" text-anchor="middle">Network</text>
      <text x="612" y="41">Phone Calls</text>
      <text x="369" y="134">Blogs</text>
      <text x="687" y="130" text-anchor="middle">Text</text>
      <text x="687" y="143" text-anchor="middle">Messages</text>
      <text x="432" y="220" text-anchor="middle">Banner</text>
      <text x="432" y="233" text-anchor="middle">Bars</text>
      <text x="622" y="228">E-mails</text>
    </g>
  </svg>
  <div class="hero-copy">
    <h1 class="hero-title">Become a Member</h1>
    <p class="hero-sub">Proin gravida nibh</p>
    <p class="hero-text">Lorem Ipsum. Proin gravida nibh vel velit auctor aliquet. Aenean sollicitudin, lorem quis bibendum auctor, nisi elit consequat ipsum, nec sagittis sem nibh id elit.</p>
  </div>
  <a class="btn btn-red signup-affiliate">Affiliate Signup</a>
  <a class="btn btn-yellow signup-login">Login</a>
</section>

<section class="wrap call">
  <svg class="call-phone" width="18" height="20" viewBox="0 0 18 20">
    <path d="M3 1 L7 1 L8 6 L5.5 7.5 Q7 12 11 14.5 L13 12 L17 13.5 L17 18 Q9 20 4 13 Q1 8 3 1 Z" fill="#777"/>
  </svg>
  <p class="call-number">Call Now: +123 456 7890</p>
  <div class="call-divider"></div>
  <p class="call-text">Signing up and getting your account configured couldn't be easier. You can be referring business our way in as little as five minutes.</p>
  <a class="btn btn-red join">Join Now!</a>
</section>

<main class="wrap content">
  <div class="col col-who">
    <h2><span class="avatar"></span>Who we are?</h2>
    <p>Lorem ipsum dolor sit amet, consectetur adipisicing elit, sed do eiusmod tempor incididunt ut labore et dolore magna aliqua. Ut enim ad minim veniam, quis nostrud exercitation ullamco laboris nisi ut aliquip ex ea commodo consequat. Duis aute irure dolor in reprehenderit in voluptate velit esse cillum dolore eu fugiat nulla pariatur. Excepteur sint occaecat</p>
  </div>
  <div class="col col-how">
    <h2><svg width="20" height="20" viewBox="0 0 20 20"><circle cx="10" cy="10" r="10" fill="#2f5aa8"/><text x="10" y="15" text-anchor="middle" font-family="Open Sans, sans-serif" font-weight="700" font-size="14" fill="#fff">?</text></svg>How Does it work?</h2>
    <ul>
      <li><svg width="9" height="7" viewBox="0 0 9 7"><path d="M0 2h5V0l4 3.5L5 7V5H0z" fill="#e8473f"/></svg>Visitor clicks on an affiliate link on your site or in an email.</li>
      <li><svg width="9" height="7" viewBox="0 0 9 7"><path d="M0 2h5V0l4 3.5L5 7V5H0z" fill="#e8473f"/></svg>The visitors IP is logged and a cookie is placed in their browser for tracking purposes.</li>
      <li><svg width="9" height="7" viewBox="0 0 9 7"><path d="M0 2h5V0l4 3.5L5 7V5H0z" fill="#e8473f"/></svg>The visitor browses our site, and may decide to order.</li>
      <li><svg width="9" height="7" viewBox="0 0 9 7"><path d="M0 2h5V0l4 3.5L5 7V5H0z" fill="#e8473f"/></svg>If the visitor orders (the order need not be placed during the same browser session--cookies and IPs are stored indefinitely), the order will be registered as a sale for you.</li>
      <li><svg width="9" height="7" viewBox="0 0 9 7"><path d="M0 2h5V0l4 3.5L5 7V5H0z" fill="#e8473f"/></svg>We will review and approve the sale.<br>You will receive commission payouts.</li>
    </ul>
  </div>
  <div class="col col-feature">
    <h2><svg width="18" height="18" viewBox="0 0 18 18"><path d="M1 9 L4 7 L7 12 Q10 5 17 0 Q11 7 7 17 Z" fill="#1f3f78"/></svg>Feature</h2>
    <div class="feature-box" style="top:71px;height:33px">Earn up to 50% commission for all products!</div>
    <div class="feature-box" style="top:121px;height:33px">High Conversion Rate = More Money.</div>
    <div class="feature-box" style="top:171px;height:33px">Long cookie duration.</div>
    <p class="feature-note">If a customer comes from your site to ours, and then comes back to purchase six months later, you get credit.</p>
  </div>
</main>

<footer class="wrap site-footer">
  <h3 class="footer-title">Contact Information</h3>
  <div class="footer-contact">
    <span><i></i>Proin gravida nibh vel velit auctor aliquet, UK.</span>
    <span><i></i>Email: info@lumacorestudio.com</span>
    <span><i></i>Email: info@lumacorestudio.com</span>
  </div>
  <div class="footer-rule"></div>
  <div class="footer-links">
    <span>Privacy</span><span>|</span><span>Policy</span><span>|</span><span>Legal Notice</span><span>|</span><span>Terms of Service</span><span>|</span><span>FAQs</span>
  </div>
  <ul class="social-list">
    <li><i></i>Friendlane</li>
    <li><i></i>Chirpline</li>
    <li><i></i>Workedin</li>
    <li><i></i>CirclePlus</li>
    <li><i></i>RSS Feeds</li>
  </ul>
</footer>
<div class="footer-base"></div>
<p class="copyright">© Copyright BLUVENDMARKET 2013</p>
</body>
</html>
```